Building Company Business Card Design

I am looking to get a business card designed for my Building Company. Please find the logo attached.

Industry/Entity Type

Business

Contact Information for Business Card

Mobile 0472 913 046
Email admin@tarrowconstructworks.com.au
Website www.tarrowconstructworks.com.au

Colors
0255a3

```html
<!DOCTYPE html>
<html lang="en">
<head>
<meta charset="utf-8">
<title>Tarrow Construct Works — Business Card</title>
<link rel="stylesheet" href="https://fonts.googleapis.com/css2?family=Montserrat:wght@500;600&family=Source+Sans+3:wght@400&display=swap">
<style>
  :root {
    --stage: #222222;
    --card-light: #f2f2f2;
    --brand-blue: #1257a6;
    --ink-blue: #0f55a3;
    --ink-grey: #5f6062;
    --ink-dark: #333333;
    --rule: #6b6b6b;
    --white: #ffffff;
  }
  * { margin: 0; padding: 0; box-sizing: border-box; }
  html, body { width: 1200px; height: 900px; overflow: hidden; }
  body { background: var(--stage); position: relative; font-family: "Source Sans 3", "Myriad Pro", sans-serif; }

  .card { position: absolute; top: 170px; width: 347px; height: 561px; text-align: center; }
  .card--front { left: 259px; background: var(--card-light); }
  .card--back { left: 631px; background: var(--brand-blue); }

  .wordmark {
    position: absolute; left: 0; right: 0;
    font-family: "Montserrat", sans-serif; font-weight: 600;
    font-size: 27px; line-height: 32px; letter-spacing: 0.5px;
    text-transform: uppercase;
  }
  .card--front .wordmark { top: 128px; color: var(--ink-blue); }
  .card--back .wordmark { top: 248px; color: var(--white); }

  .holder {
    position: absolute; top: 360px; left: 0; right: 0;
    font-family: "Montserrat", sans-serif; font-weight: 600;
    font-size: 21px; letter-spacing: 0.3px; text-transform: uppercase;
  }
  .holder__first { color: var(--ink-blue); }
  .holder__last { color: var(--ink-grey); }
  .holder__role {
    position: absolute; top: 387px; left: 0; right: 0;
    font-size: 15px; color: var(--ink-dark);
  }
  .divider {
    position: absolute; top: 424px; left: 93px; width: 161px;
    height: 1px; background: var(--rule);
  }
  .contact-icons {
    position: absolute; top: 447px; left: 0; right: 0;
    display: flex; justify-content: center; gap: 4px;
  }
  .contact-icons svg { width: 12px; height: 12px; fill: var(--ink-blue); }
  .contact-list {
    position: absolute; top: 465px; left: 0; right: 0;
    list-style: none; font-size: 15px; line-height: 21px; color: var(--ink-dark);
  }
  .back-site {
    position: absolute; top: 498px; left: 0; right: 0;
    font-size: 15.5px; color: var(--white);
  }
</style>
</head>
<body>
  <section class="card card--front">
    <div class="wordmark">Tarrow<br>Construct Works</div>

    <div class="holder"><span class="holder__first">Marcus</span> <span class="holder__last">Hale</span></div>
    <div class="holder__role">Managing Director</div>
    <div class="divider"></div>

    <div class="contact-icons">
      <svg viewBox="0 0 24 24" aria-label="Phone"><path d="M6.6 10.8c1.4 2.8 3.8 5.1 6.6 6.6l2.2-2.2c.3-.3.7-.4 1-.2 1.1.4 2.3.6 3.6.6.6 0 1 .4 1 1V20c0 .6-.4 1-1 1C10.6 21 3 13.4 3 4c0-.6.4-1 1-1h3.5c.6 0 1 .4 1 1 0 1.3.2 2.5.6 3.6.1.3 0 .7-.2 1z"/></svg>
      <svg viewBox="0 0 24 24" aria-label="Email"><path d="M2 5h20v14H2z M3.5 6.5 12 13l8.5-6.5" fill="var(--ink-blue)" stroke="var(--card-light)" stroke-width="1.5"/></svg>
      <svg viewBox="0 0 24 24" aria-label="Website"><circle cx="12" cy="12" r="10"/><path d="M2 12h20M12 2c3 3 3 17 0 20M12 2c-3 3-3 17 0 20" fill="none" stroke="var(--card-light)" stroke-width="1.4"/></svg>
    </div>
    <ul class="contact-list">
      <li>0472 913 046</li>
      <li>admin@tarrowconstructworks.com.au</li>
      <li>www.tarrowconstructworks.com.au</li>
    </ul>
  </section>

  <section class="card card--back">
    <div class="wordmark">Tarrow<br>Construct Works</div>
    <div class="back-site">www.tarrowconstructworks.com.au</div>
  </section>
</body>
</html>
```